Kestrelwood Pathways Agency business cards

Australian company about to start offering its services. We recruit international students to come to study English, vocational education and postgraduate courses in Australia. We help them find the institution and select the right city they want to come to Australia. We are a young, online oriented and supportive agency. Our clients are between 18 and 35 years old, mainly University students, young professionals or people with work experience. We provide much more information that any other agency offer. We administrate a Facebook group with more than 11.000 members that daily ask questions about general information when coming to Australia, while they are here and even after they leave the country

Target Market(s)

International students from South America, Central America and Europe

Industry/Entity Type

Student

Contact Information for Business Card

Tomas Brevik
Managing Director
tomas@velmorin.com.au
www.velmorin.com.au
+61 491058263
Melbourne, Australia

Font styles to use
Serif
Sans Serif

Colors

Designer to choose colors to be used in the design.

Requirements
Must have
• Horizontal design
• Standard business card size and shape. If font uses green or yellow colours, they will have to match the ones from the logo
Nice to have
• UPDATE: Use the contents of the green image to design one of the card sides. Use our logo in the background of that side as watermark.
• Passport image, or immigration stamps. A picture of the Yarra River (from Melbourne) would be cool as well.
Should not have
• Non-standard business card size and shape
• Not black as the background colour of any sides as we are not a VIP agency or a hight class service. We are orientes to young people and they like colours, pictures, something attractive.
• Vertical design
• NO YELLOW or BLACK AS THE BACKGROUND COLOUR OF ANY SIDE OF THE BIZ CARD

```html
<!DOCTYPE html>
<html lang="en">
<head>
<meta charset="utf-8">
<title>Kestrelwood Pathways Agency – Business Cards</title>
<link rel="stylesheet" href="https://fonts.googleapis.com/css2?family=Open+Sans:wght@400;600;700&display=swap">
<style>
  :root {
    --brand-green: #155e3b;
    --brand-green-light: #1f6d48;
    --brand-yellow: #e4b625;
    --paper: #ffffff;
    --ink-grey: #555a57;
    --backdrop: #d9dbd9;
    --sky-top: #7fa9d6;
    --sky-glow: #e9e3c4;
    --river: #3f6f92;
  }
  * { box-sizing: border-box; margin: 0; padding: 0; }
  html, body {
    width: 1200px; height: 1000px; overflow: hidden;
    background: var(--backdrop);
    font-family: "Open Sans", Arial, sans-serif;
  }
  .stage { position: relative; width: 1200px; height: 1000px; }
  .card {
    position: absolute; left: 220px; width: 761px;
    overflow: hidden;
    box-shadow: 0 4px 14px rgba(0,0,0,0.25);
  }
  /* Front */
  .card-front {
    top: 50px; height: 433px;
    background: linear-gradient(120deg, var(--brand-green) 40%, var(--brand-green-light) 100%);
  }
  .front-brand {
    position: absolute; left: 0; right: 0; top: 215px;
    display: flex; align-items: center; justify-content: center; gap: 14px;
  }
  .brand-dot {
    width: 22px; height: 22px; border-radius: 50%;
    background: var(--brand-yellow);
  }
  .front-brand .brand-name {
    font-size: 54px; font-weight: 700; color: var(--paper); letter-spacing: 0.5px;
  }
  .tagline {
    position: absolute; left: 0; right: 0; top: 377px;
    text-align: center; color: var(--paper); font-size: 16px;
  }
  /* Back */
  .card-back { top: 523px; height: 436px; background: var(--paper); }
  .back-art { position: absolute; inset: 0; }
  .back-brand {
    position: absolute; left: 37px; top: 92px;
    display: flex; align-items: center; gap: 10px;
  }
  .back-brand .brand-dot { width: 18px; height: 18px; }
  .back-brand .brand-name {
    font-size: 40px; font-weight: 700; color: var(--brand-green);
  }
  .name-bar {
    position: absolute; left: 0; top: 244px; width: 10px; height: 37px;
    background: var(--brand-yellow);
  }
  .person { position: absolute; left: 37px; top: 240px; }
  .person-name { font-size: 21px; font-weight: 700; color: var(--brand-green); line-height: 1.2; }
  .person-title { font-size: 15.5px; color: var(--ink-grey); line-height: 1.3; }
  .contacts { position: absolute; left: 37px; top: 311px; list-style: none; }
  .contacts li {
    display: flex; align-items: center; gap: 7px;
    font-size: 16px; color: var(--ink-grey); height: 25px;
  }
  .contacts svg { width: 13px; height: 13px; fill: var(--brand-yellow); flex: none; }
</style>
</head>
<body>
<main class="stage">

  <section class="card card-front" aria-label="Business card front">
    <div class="front-brand">
      <span class="brand-dot"></span>
      <span class="brand-name">Kestrelwood</span>
    </div>
    <p class="tagline">Hacemos más por ti!</p>
  </section>

  <section class="card card-back" aria-label="Business card back">
    <svg class="back-art" viewBox="0 0 761 436" width="761" height="436">
      <defs>
        <linearGradient id="cityScene" x1="0" y1="0" x2="0" y2="1">
          <stop offset="0" stop-color="var(--sky-top)"/>
          <stop offset="0.3" stop-color="var(--sky-glow)"/>
          <stop offset="0.55" stop-color="#6d8a74"/>
          <stop offset="1" stop-color="var(--river)"/>
        </linearGradient>
      </defs>
      <path class="curve-band" d="M430,0 C355,130 360,330 470,436 L761,436 L761,0 Z" fill="var(--brand-green)"/>
      <path d="M455,0 C390,130 400,320 520,436 L761,436 L761,0 Z" fill="url(#cityScene)"
            role="img" aria-label="Photo of the Melbourne skyline over the Yarra River at sunset"/>
    </svg>

    <div class="back-brand">
      <span class="brand-dot"></span>
      <span class="brand-name">Kestrelwood</span>
    </div>

    <span class="name-bar"></span>
    <div class="person">
      <p class="person-name">Tomas Brevik</p>
      <p class="person-title">Managing Director</p>
    </div>

    <ul class="contacts">
      <li>
        <svg viewBox="0 0 16 16" aria-hidden="true"><path d="M3.5 1l2.5 3-1.5 2c1 2 3 4 5 5l2-1.5 3 2.5-1.5 2.5C8 16 0 8 1 2.5z"/></svg>
        +61 491058263
      </li>
      <li>
        <svg viewBox="0 0 16 16" aria-hidden="true"><path d="M1 3h14v10H1z M1 3l7 6 7-6" stroke="#fff" stroke-width="1.2"/></svg>
        tomas@velmorin.com.au
      </li>
      <li>
        <svg viewBox="0 0 16 16" aria-hidden="true"><circle cx="8" cy="8" r="7"/><path d="M1 8h14M8 1c-3 4-3 10 0 14M8 1c3 4 3 10 0 14" stroke="#fff" stroke-width="1" fill="none"/></svg>
        www.velmorin.com.au
      </li>
    </ul>
  </section>

</main>
</body>
</html>
```